KiteSurf Weather App Forecast Screen re-design (1 Screen)

We are redesigning our application, BreezeLedger. Our main screen is the forecast screen. The forecast screen presents the forecast for multiple places for the selected day.

Intro
-----

The user has a list of favorite spots that he is monitoring. Then he selects the date that he wants to get the forecast. The forecast screen presents a list of all the spots and a summary of the weather conditions. Spots are sorted by weather conditions. At the top, he gets the spot with the best weather conditions. We have an algorithm that can evaluate whether given weather conditions are good or not. When they are good we indicate that to the user.

Current Solution
------------------

Our current screen looks like the attachment named: "Current Forecast Screen.jpeg"

There is also a landscape version, which contains a bit more data: "Current Forecast Screen Lanscape.jpeg". The landscape one is a bit funny, as it is taken from an Norvo Q7 and the app was not designed for it at the time.

The bars that you see for each hour use our algorithm to display whether the conditions are good:

- When the color is gray the conditions are not good
- When the color is yellow there are light wind conditions
- When the color is green there are good
- When the color is red the wind is very strong
- The height of the bar indicates wind strength

More Info
-----------

The detailed forecast screen is also attached so you can get a bit more context, "DetailedForecast.jpeg"

An example from an application that has a similar chart is attached, "SimilarApp.jpeg". I have circled the chart with red.

Future Solution
------------------

(See note.jpeg)

We want to create a page that contains more information and passes a better message to our users.

The elements that are important and we want to present to the user are the following:

1. Wind. (The most important)
It contains two elements: strength and direction.

1.1 Wind Strength.
Good wind strength is anything between 10-45 knots (measurement unit like km/h). The best representation with a color palette.
Gray will be the color used when the strength is not between 10-45.
The palette should start with yellow at 10 knots, then move toward green for 22knots and finally go towards red for 45 knots.

1.2 Wind Direction.
There are good wind directions that we can kite and directions that is is not possible.
Can be presented by an arrow that points in the direction the wind is blowing to. The color of the arrow will be green when the direction is good, yellow when it is average and gray when it is not good.

My thought for portrait mode is to use an arrow point for the direction and the color of the arrow to represent the strength. Solution number 2 on my notes. Then for landscape, we could use both a number and an arrow like number 4 on my notes.

2. Wave.
It contains three elements: height, period and direction. It is not displayed to all of our users only the ones that have selected the wave riding option.

2.1 Height is represented by a number. Ex. 1.2 meters or 2 foot.
2.2 Period is represented in seconds. Ex. 12 seconds.
2.3 Directions is an arrow that points to the direction the wave is coming from.

Again the solution should be like the wind. Arrow for direction and the color of the arrow for height. The palette here should be something with different blue colors.

3. Tide height. (Optional for tidal spots, as not all spots have tides)

The best way to represent that it through a graph. I would also like to see an alternative, where we have three symbols for low, mid and high tide.

4. General Weather. Rain/Snow and temperature.

This should be represented by a sun/cloud/rain symbol. If it is very cold the symbol can also contain an ice sign on the background.

---------

This is a guideline creativity will be valued. Maybe there is another way to do it that I have not thought about.

The winner of the competition will have to send us all graphics used in vector format, so we can input them to our xCode project.

Finally the person that wins the competition will be the first one to be considered for the redesign of the rest of our application.

Target Market(s)

Kitesurfers

Font styles to use
Sans Serif

Colors

Designer to choose colors to be used in the design.

Requirements
Must have
• It should be minimal and clearly communicate the weather forecast to my users. It should be user friendly.
Nice to have
• Communicative color palettes for both wind strength, tide and waves
Should not have
• Hard to understand UI

```html
<!DOCTYPE html>
<html lang="en">
<head>
<meta charset="utf-8">
<title>BreezeLedger – Forecast</title>
<link rel="stylesheet" href="https://fonts.googleapis.com/css2?family=Inter:wght@400;500;700&display=swap">
<style>
  :root{
    --page-bg:#eceff3;
    --surface:#ffffff;
    --ink:#2a4c94;
    --divider:#dfe6ee;
    --chevron:#d3dcea;
    --header-sunny:#3a91e5;
    --header-cloudy:#838383;
    --header-storm:#264e9a;
    --temp-low:#9cc4f0;
    --wind-good:#6bb51d;
    --wind-off:#c4c4c4;
    --wind-strong:#d8304a;
    --wind-light:#f3cf00;
    --wave:#93c0f0;
    --tide-high:#264e9a;
    --tide-low:#c4c4c4;
    --sun:#f7d117;
  }
  *{box-sizing:border-box;margin:0;padding:0}
  html,body{width:675px;height:1200px;overflow:hidden}
  body{background:var(--page-bg);font-family:"Inter",sans-serif;color:var(--ink);position:relative}

  .hour-bar{position:absolute;left:0;top:0;width:675px;height:84px;background:var(--surface);
    box-shadow:0 2px 6px rgba(40,60,90,.12);z-index:2}
  .hour-bar__label{position:absolute;left:58px;top:45px;transform:translateY(-50%);font-size:24px}
  .hour-bar__nav{position:absolute;top:26px}
  .hour-bar__nav--prev{left:176px}
  .hour-bar__nav--next{left:632px}
  .hour-bar__hour{position:absolute;top:45px;transform:translate(-50%,-50%);font-size:24px}

  .spot-card{position:absolute;left:27px;width:621px;height:389px;background:var(--surface);
    border-radius:27px;overflow:hidden;box-shadow:0 4px 14px rgba(40,60,90,.08)}
  .spot-card--cape{top:108px}
  .spot-card--bigbay{top:528px}
  .spot-card--loutsa{top:948px}

  .spot-header{height:94px;display:flex;align-items:center;padding:0 31px 0 30px;color:#fff}
  .spot-header--sunny{background:var(--header-sunny)}
  .spot-header--cloudy{background:var(--header-cloudy)}
  .spot-header--storm{background:var(--header-storm)}
  .spot-name{font-size:34px;font-weight:700;flex:1}
  .spot-weather{width:66px;height:66px;margin-right:26px}
  .spot-temp-low{font-size:27px;color:var(--temp-low);margin-right:10px}
  .spot-temp-high{font-size:34px}

  .metric-row{position:relative;margin:0 27px 0 34px;border-bottom:1px solid var(--divider)}
  .metric-row:last-child{border-bottom:none}
  .metric-row--wind{height:98px}
  .metric-row--wave{height:100px}
  .metric-row--tide{height:97px}
  .metric-icon{position:absolute;left:0;top:50%;transform:translateY(-50%)}
  .metric-label{position:absolute;left:61px;top:50%;transform:translateY(-50%);font-size:25px}

  .metric-values{position:absolute;left:149px;top:0;display:grid;grid-template-columns:repeat(5,80px)}
  .value{display:flex;flex-direction:column;align-items:center;font-size:18px;line-height:24px}
  .metric-row--wind .value{padding-top:22px}
  .metric-row--wind .value svg{margin-bottom:6px}
  .metric-row--wave .value{padding-top:12px;color:var(--wave)}
  .metric-row--wave .value svg{margin-bottom:3px}
  .value--good{color:var(--wind-good)}
  .value--off{color:var(--wind-off)}
  .value--strong{color:var(--wind-strong)}
  .value--light{color:var(--wind-light)}

  .tide-chart{position:absolute;left:149px;top:0}
</style>
</head>
<body>
<svg width="0" height="0" style="position:absolute">
  <defs>
    <symbol id="dir-arrow" viewBox="-12 -12 24 24">
      <path d="M0 -11 L9 10 L0 5 L-9 10 Z" fill="currentColor"/>
    </symbol>
    <symbol id="icon-wind" viewBox="0 0 40 30">
      <g fill="none" stroke="var(--wave)" stroke-width="2" stroke-linecap="round">
        <path d="M2 9 H26 a4 4 0 1 0 -4 -4"/>
        <path d="M6 15 H34"/>
        <path d="M2 21 H24 a4 4 0 1 1 -4 4"/>
      </g>
    </symbol>
    <symbol id="icon-wave" viewBox="0 0 46 20">
      <path d="M2 14 c4 -8 8 -8 10 -2 c2 6 6 6 9 0 c3 -6 7 -6 9 0 c2 6 6 6 9 0 c2 -4 4 -4 5 -3" fill="none" stroke="var(--wave)" stroke-width="2" stroke-linecap="round"/>
    </symbol>
    <symbol id="icon-tide" viewBox="0 0 44 32">
      <g fill="none" stroke="var(--wave)" stroke-width="2" stroke-linecap="round">
        <path d="M22 14 V2 M17 7 L22 2 L27 7"/>
        <path d="M2 20 c3 -3 5 -3 8 0 s5 3 8 0 s5 -3 8 0 s5 3 8 0 s5 -3 8 0"/>
        <path d="M2 27 c3 -3 5 -3 8 0 s5 3 8 0 s5 -3 8 0 s5 3 8 0 s5 -3 8 0"/>
      </g>
    </symbol>
  </defs>
</svg>

<header class="hour-bar">
  <span class="hour-bar__label">Hour</span>
  <svg class="hour-bar__nav hour-bar__nav--prev" width="18" height="38" viewBox="0 0 18 38"><path d="M15 2 L3 19 L15 36" fill="none" stroke="var(--chevron)" stroke-width="3" stroke-linecap="round"/></svg>
  <span class="hour-bar__hour" style="left:252px">08</span>
  <span class="hour-bar__hour" style="left:331px">09</span>
  <span class="hour-bar__hour" style="left:410px">10</span>
  <span class="hour-bar__hour" style="left:486px">11</span>
  <span class="hour-bar__hour" style="left:567px">12</span>
  <svg class="hour-bar__nav hour-bar__nav--next" width="18" height="38" viewBox="0 0 18 38"><path d="M3 2 L15 19 L3 36" fill="none" stroke="var(--chevron)" stroke-width="3" stroke-linecap="round"/></svg>
</header>

<!-- Cape Town -->
<section class="spot-card spot-card--cape">
  <div class="spot-header spot-header--sunny">
    <h2 class="spot-name">Cape town</h2>
    <svg class="spot-weather" viewBox="0 0 66 66" aria-label="Sunny">
      <circle cx="33" cy="33" r="13" fill="none" stroke="var(--sun)" stroke-width="5"/>
      <g stroke="var(--sun)" stroke-width="4" stroke-linecap="round">
        <path d="M33 4v7M33 55v7M4 33h7M55 33h7M12.5 12.5l5 5M48.5 48.5l5 5M12.5 53.5l5-5M48.5 17.5l5-5"/>
        <path d="M22 6.5l2 5M42 54.5l2 5M6.5 44l5-2M54.5 24l5-2M44 6.5l-2 5M24 54.5l-2 5M6.5 22l5 2M54.5 42l5 2"/>
      </g>
    </svg>
    <span class="spot-temp-low">10°</span><span class="spot-temp-high">15°</span>
  </div>
  <div class="metric-row metric-row--wind">
    <svg class="metric-icon" width="36" height="27"><use href="#icon-wind"/></svg>
    <span class="metric-label">Wind</span>
    <div class="metric-values">
      <div class="value value--good"><svg width="24" height="24" style="transform:rotate(90deg)"><use href="#dir-arrow"/></svg>22kn</div>
      <div class="value value--off"><svg width="24" height="24" style="transform:rotate(20deg)"><use href="#dir-arrow"/></svg>6kn</div>
      <div class="value value--strong"><svg width="24" height="24" style="transform:rotate(180deg)"><use href="#dir-arrow"/></svg>45kn</div>
      <div class="value value--off"><svg width="24" height="24" style="transform:rotate(205deg)"><use href="#dir-arrow"/></svg>2kn</div>
      <div class="value value--light"><svg width="24" height="24" style="transform:rotate(150deg)"><use href="#dir-arrow"/></svg>17kn</div>
    </div>
  </div>
  <div class="metric-row metric-row--wave">
    <svg class="metric-icon" width="44" height="19"><use href="#icon-wave"/></svg>
    <span class="metric-label">Wave</span>
    <div class="metric-values">
      <div class="value"><svg width="24" height="24" style="color:var(--wave);transform:rotate(90deg)"><use href="#dir-arrow"/></svg>1.2<br>12s</div>
      <div class="value"><svg width="24" height="24" style="color:var(--wave);transform:rotate(20deg)"><use href="#dir-arrow"/></svg>2.2<br>15s</div>
      <div class="value"><svg width="24" height="24" style="color:var(--wave);transform:rotate(270deg)"><use href="#dir-arrow"/></svg>1.4<br>26s</div>
      <div class="value"><svg width="24" height="24" style="color:var(--wave);transform:rotate(20deg)"><use href="#dir-arrow"/></svg>4.1<br>18s</div>
      <div class="value"><svg width="24" height="24" style="color:var(--wave);transform:rotate(20deg)"><use href="#dir-arrow"/></svg>1.1<br>34s</div>
    </div>
  </div>
  <div class="metric-row metric-row--tide">
    <svg class="metric-icon" width="40" height="29"><use href="#icon-tide"/></svg>
    <span class="metric-label">Tide</span>
    <svg class="tide-chart" width="410" height="97" viewBox="0 0 410 97" aria-label="Tide levels by hour">
      <g stroke="var(--divider)" stroke-dasharray="4 4"><path d="M0 27H410M0 48H410M0 70H410"/></g>
      <circle cx="74" cy="48" r="5" fill="var(--wave)"/>
      <circle cx="153" cy="27" r="5" fill="var(--tide-high)"/>
      <circle cx="234" cy="48" r="5" fill="var(--wave)"/>
      <circle cx="313" cy="70" r="5" fill="var(--tide-low)"/>
      <circle cx="393" cy="48" r="5" fill="var(--wave)"/>
    </svg>
  </div>
</section>

<!-- Big Bay -->
<section class="spot-card spot-card--bigbay">
  <div class="spot-header spot-header--cloudy">
    <h2 class="spot-name">Big bay</h2>
    <svg class="spot-weather" viewBox="0 0 66 66" aria-label="Sun with rain clouds">
      <g fill="none" stroke="#b5b5b5" stroke-width="3" stroke-linecap="round">
        <path d="M36 18a12 12 0 0 1 20 12"/>
        <path d="M45 5v5M58 10l-4 4M63 24h-5M34 10l4 4"/>
        <path d="M14 44a9 9 0 0 1 2-18a13 13 0 0 1 25-2a10 10 0 0 1 8 20Z"/>
        <path d="M16 50l-2 5M24 50l-2 5M32 50l-2 5M40 50l-2 5M20 58l-2 5M28 58l-2 5M36 58l-2 5"/>
      </g>
    </svg>
    <span class="spot-temp-low">10°</span><span class="spot-temp-high">15°</span>
  </div>
  <div class="metric-row metric-row--wind">
    <svg class="metric-icon" width="36" height="27"><use href="#icon-wind"/></svg>
    <span class="metric-label">Wind</span>
    <div class="metric-values">
      <div class="value value--good"><svg width="24" height="24" style="transform:rotate(90deg)"><use href="#dir-arrow"/></svg>22kn</div>
      <div class="value value--off"><svg width="24" height="24" style="transform:rotate(20deg)"><use href="#dir-arrow"/></svg>6kn</div>
      <div class="value value--strong"><svg width="24" height="24" style="transform:rotate(180deg)"><use href="#dir-arrow"/></svg>45kn</div>
      <div class="value value--off"><svg width="24" height="24" style="transform:rotate(205deg)"><use href="#dir-arrow"/></svg>2kn</div>
      <div class="value value--light"><svg width="24" height="24" style="transform:rotate(150deg)"><use href="#dir-arrow"/></svg>17kn</div>
    </div>
  </div>
  <div class="metric-row metric-row--wave">
    <svg class="metric-icon" width="44" height="19"><use href="#icon-wave"/></svg>
    <span class="metric-label">Wave</span>
    <div class="metric-values">
      <div class="value"><svg width="24" height="24" style="color:var(--wave);transform:rotate(90deg)"><use href="#dir-arrow"/></svg>1.2<br>12s</div>
      <div class="value"><svg width="24" height="24" style="color:var(--wave);transform:rotate(20deg)"><use href="#dir-arrow"/></svg>2.2<br>15s</div>
      <div class="value"><svg width="24" height="24" style="color:var(--wave);transform:rotate(270deg)"><use href="#dir-arrow"/></svg>1.4<br>26s</div>
      <div class="value"><svg width="24" height="24" style="color:var(--wave);transform:rotate(20deg)"><use href="#dir-arrow"/></svg>4.1<br>18s</div>
      <div class="value"><svg width="24" height="24" style="color:var(--wave);transform:rotate(20deg)"><use href="#dir-arrow"/></svg>1.1<br>34s</div>
    </div>
  </div>
  <div class="metric-row metric-row--tide">
    <svg class="metric-icon" width="40" height="29"><use href="#icon-tide"/></svg>
    <span class="metric-label">Tide</span>
    <svg class="tide-chart" width="410" height="97" viewBox="0 0 410 97" aria-label="Tide levels by hour">
      <g stroke="var(--divider)" stroke-dasharray="4 4"><path d="M0 27H410M0 48H410M0 70H410"/></g>
      <circle cx="74" cy="48" r="5" fill="var(--wave)"/>
      <circle cx="153" cy="27" r="5" fill="var(--tide-high)"/>
      <circle cx="234" cy="48" r="5" fill="var(--wave)"/>
      <circle cx="313" cy="70" r="5" fill="var(--tide-low)"/>
      <circle cx="393" cy="48" r="5" fill="var(--wave)"/>
    </svg>
  </div>
</section>

<!-- Loutsa -->
<section class="spot-card spot-card--loutsa">
  <div class="spot-header spot-header--storm">
    <h2 class="spot-name">Loutsa</h2>
    <svg class="spot-weather" viewBox="0 0 66 66" aria-label="Thunderstorm">
      <g fill="none" stroke="#4aa3f0" stroke-width="3.5" stroke-linecap="round" stroke-linejoin="round">
        <path d="M22 44H14a10 10 0 0 1 0-20a16 16 0 0 1 30-4a12 12 0 0 1 8 24H42"/>
      </g>
      <path d="M34 36l-6 12h6l-3 10l9-14h-6l3-8Z" fill="#4aa3f0"/>
    </svg>
    <span class="spot-temp-low">10°</span><span class="spot-temp-high">15°</span>
  </div>
  <div class="metric-row metric-row--wind">
    <svg class="metric-icon" width="36" height="27"><use href="#icon-wind"/></svg>
    <span class="metric-label">Wind</span>
    <div class="metric-values">
      <div class="value value--good"><svg width="24" height="24" style="transform:rotate(90deg)"><use href="#dir-arrow"/></svg>22kn</div>
      <div class="value value--off"><svg width="24" height="24" style="transform:rotate(20deg)"><use href="#dir-arrow"/></svg>6kn</div>
      <div class="value value--strong"><svg width="24" height="24" style="transform:rotate(180deg)"><use href="#dir-arrow"/></svg>45kn</div>
      <div class="value value--off"><svg width="24" height="24" style="transform:rotate(205deg)"><use href="#dir-arrow"/></svg>2kn</div>
      <div class="value value--light"><svg width="24" height="24" style="transform:rotate(150deg)"><use href="#dir-arrow"/></svg>17kn</div>
    </div>
  </div>
  <div class="metric-row metric-row--wave">
    <svg class="metric-icon" width="44" height="19"><use href="#icon-wave"/></svg>
    <span class="metric-label">Wave</span>
    <div class="metric-values">
      <div class="value"><svg width="24" height="24" style="color:var(--wave);transform:rotate(90deg)"><use href="#dir-arrow"/></svg>1.2<br>12s</div>
      <div class="value"><svg width="24" height="24" style="color:var(--wave);transform:rotate(20deg)"><use href="#dir-arrow"/></svg>2.2<br>15s</div>
      <div class="value"><svg width="24" height="24" style="color:var(--wave);transform:rotate(270deg)"><use href="#dir-arrow"/></svg>1.4<br>26s</div>
      <div class="value"><svg width="24" height="24" style="color:var(--wave);transform:rotate(20deg)"><use href="#dir-arrow"/></svg>4.1<br>18s</div>
      <div class="value"><svg width="24" height="24" style="color:var(--wave);transform:rotate(20deg)"><use href="#dir-arrow"/></svg>1.1<br>34s</div>
    </div>
  </div>
</section>
</body>
</html>
```